Mobile and Web design for Remote Skin Condition Service

A new web service that allows patients to upload photos for doctors to review. I need the designs for both mobile (NOT native app) and desktop versions. Key pages are provided in the mockups, and all major form elements are required.
Overall branding and design needed.

We are building an online system that allows patients to connect with a skin doctors.

Users will access the website (typically, but not exclusively via a mobile phone), register, upload photos, answer a few questions and pay to submit their details to a doctor.

The doctor will access the website via a desktop browser and review the case.

The patient’s user flow should be optimised for mobile. It should be usable on desktop too.

The doctor’s user flow should be optimised for desktop. It should be usable on mobile too.

Currently there are no branding restrictions, and no logo, so please be creative.

The site has to look professional, clean and easy to use.
There will be limited text on the pages.
Buttons should be prominent - but they should also obviously be buttons.

Attached are a selection of screens showing most of the functionality of the process - it is not all of the screens of the process but should give the developers enough range and examples.

Target Market(s)

Any user with a skin condition

Industry/Entity Type

Healthcare

Number of Pages Required

5+ page

Colors

Designer to choose colors to be used in the design.

Requirements
Must have
• Mobile and desktop versions of the key pages as per the brief.
• Should be obvious to use - eg the photo upload and camera functions should be standard

```html
<!DOCTYPE html>
<html lang="en">
<head>
<meta charset="utf-8">
<title>Clarivo – Mobile Home</title>
<link rel="stylesheet" href="https://fonts.googleapis.com/css2?family=Open+Sans:wght@300;400;600;700&display=swap">
<style>
  :root {
    --teal: #6fbbbb;
    --teal-soft: #eaf8f8;
    --teal-line: #d9f0f0;
    --heading: #5d6d7c;
    --body: #7a8590;
    --ink: #3d4a55;
    --page: #f6f7f8;
    --screen: #ffffff;
    --link: #1a7be0;
    --dot: #d9dcdf;
  }
  * { box-sizing: border-box; margin: 0; padding: 0; }
  html, body { width: 1200px; height: 2807px; overflow: hidden; }
  body { background: var(--page); font-family: "Open Sans", sans-serif; position: relative; }

  .screen {
    position: absolute; left: 266px; top: 225px; width: 663px; height: 2361px;
    background: var(--screen); box-shadow: 0 6px 40px rgba(40,60,80,.08);
  }
  .header { position: absolute; left: 0; top: 0; width: 100%; height: 92px; }
  .brand {
    position: absolute; left: 29px; top: 26px; font-size: 27px; font-weight: 700;
    letter-spacing: 2.5px; color: var(--teal); line-height: 1;
  }
  .btn-login {
    position: absolute; left: 436px; top: 20px; width: 125px; height: 52px; border-radius: 8px;
    background: var(--teal); color: #fff; font-size: 23px; font-weight: 400;
    display: flex; align-items: center; justify-content: center;
  }
  .btn-menu {
    position: absolute; left: 576px; top: 19px; width: 56px; height: 54px; border-radius: 8px;
    border: 2px solid var(--teal); display: flex; flex-direction: column;
    justify-content: center; align-items: center; gap: 7px;
  }
  .btn-menu span { width: 32px; height: 2px; background: var(--teal); border-radius: 1px; }

  .hero {
    position: absolute; left: 0; top: 92px; width: 100%; height: 374px;
    background: linear-gradient(120deg, #ffffff 0%, #f3e3da 35%, #d9b7a4 60%, #6b5448 85%, #2c2320 100%);
  }

  .section-title {
    position: absolute; left: 0; width: 100%; text-align: center;
    font-size: 44px; font-weight: 300; color: var(--heading); line-height: 1;
  }
  .title-care { top: 520px; }
  .title-connected { top: 1486px; }

  .intro {
    position: absolute; left: 34px; right: 34px; top: 600px; height: 193px; overflow: hidden;
    text-align: center; font-size: 23.5px; font-weight: 300; line-height: 38.6px; color: var(--body);
  }

  .feature {
    position: absolute; left: 29px; width: 602px; height: 177px; border: 2px solid var(--teal-line);
    border-radius: 6px; box-shadow: 0 4px 18px rgba(111,187,187,.08);
  }
  .feature-1 { top: 856px; } .feature-2 { top: 1052px; } .feature-3 { top: 1251px; }
  .feature-icon {
    position: absolute; left: 19px; top: 22px; width: 129px; height: 129px; border-radius: 50%;
    background: var(--teal-soft);
  }
  .feature-text {
    position: absolute; left: 186px; right: 20px; top: 50%; transform: translateY(-50%);
    font-size: 24px; line-height: 39px; color: var(--ink);
  }

  .testimonial {
    position: absolute; left: 29px; top: 1586px; width: 602px; height: 470px;
    border: 2px solid var(--teal-line); border-radius: 6px; text-align: center;
    box-shadow: 0 4px 18px rgba(111,187,187,.08);
  }
  .avatar {
    position: absolute; left: 243px; top: 45px; width: 114px; height: 114px; border-radius: 50%;
    background: radial-gradient(circle at 50% 40%, #c9a891 0%, #8c7160 45%, #3b3736 100%);
    box-shadow: 0 0 0 8px #eef8f8;
  }
  .testimonial-name {
    position: absolute; left: 0; width: 100%; top: 184px; font-size: 27px; color: var(--ink);
  }
  .testimonial-quote {
    position: absolute; left: 36px; right: 26px; top: 240px; height: 118px; overflow: hidden;
    font-size: 23.5px; font-weight: 300; line-height: 38.6px; color: var(--body);
  }
  .carousel-dots { position: absolute; left: 0; width: 100%; top: 424px; display: flex; justify-content: center; gap: 14px; }
  .carousel-dots span { width: 15px; height: 15px; border-radius: 50%; background: var(--dot); }
  .carousel-dots .active { background: var(--teal); }

  .btn-diagnose {
    position: absolute; left: 29px; top: 2103px; width: 602px; height: 87px; border-radius: 6px;
    background: var(--teal); color: #fff; font-size: 27px; font-weight: 600;
    display: flex; align-items: center; justify-content: center;
  }

  .footer { position: absolute; left: 29px; width: 602px; top: 2230px; border-top: 2px solid #eceeef; text-align: center; }
  .copyright { margin-top: 35px; font-size: 18px; font-weight: 700; color: var(--ink); }
  .legal-links { margin-top: 18px; font-size: 18px; font-weight: 700; color: var(--ink); }
  .legal-links a { color: var(--link); text-decoration: underline; }
</style>
</head>
<body>
<main class="screen">
  <header class="header">
    <div class="brand">CLARIVO</div>
    <a class="btn-login">Login</a>
    <div class="btn-menu" aria-label="Menu"><span></span><span></span><span></span></div>
  </header>

  <div class="hero" role="img" aria-label="Photo of a smiling woman with clear skin"></div>

  <h1 class="section-title title-care">We Care About Your Health</h1>
  <p class="intro">There are many variations of passages of Lorem Ipsum available, but the majority have suffered alteration in some form, by injected humour, or randomised words which don't look even slightly believable. If you are going to use a passage of Lorem Ipsum, you need to be</p>

  <section class="feature feature-1">
    <div class="feature-icon" role="img" aria-label="Line illustration of two people in a queue"></div>
    <p class="feature-text">The waiting is finally over! no waiting in long queues at clinics</p>
  </section>

  <section class="feature feature-2">
    <div class="feature-icon" role="img" aria-label="Line illustration of a person consulting from home"></div>
    <p class="feature-text">Traffic is not a problem anymore, consult a doctor from home</p>
  </section>

  <section class="feature feature-3">
    <div class="feature-icon" role="img" aria-label="Line illustration of a hand holding money"></div>
    <p class="feature-text">Simple, convenient &amp; affordable</p>
  </section>

  <h2 class="section-title title-connected">Connected to Serve Better</h2>

  <section class="testimonial">
    <div class="avatar" role="img" aria-label="Portrait photo of the reviewer"></div>
    <p class="testimonial-name">Anika Solis</p>
    <p class="testimonial-quote">Lorem Ipsum is simply dummy text of the printing and typesetting industry. Lorem Ipsum has been the industry's standard dummy text ever since the</p>
    <div class="carousel-dots"><span></span><span class="active"></span><span></span></div>
  </section>

  <a class="btn-diagnose">Get Diagnosed</a>

  <footer class="footer">
    <p class="copyright">© 2020 Clarivo. All rights reserved.</p>
    <p class="legal-links"><a>Privacy Police</a> &nbsp;-&nbsp; <a>Terms of Service</a></p>
  </footer>
</main>
</body>
</html>
```